Lanternfield Drinks business cards

We need a business card design for our new logo. The company is modern, progressive, professional, yet approachable. The key products are ready to drink bottles and cans of coffee based beverages.
These cards will be a critical part of the first impression made by our sales organization, business development team, and all external facing personnel.
Card can be a vertical or horizontal orientation.

Target Market(s)

Customers, suppliers, business partners

Industry/Entity Type

Business

Contact Information for Business Card

Business cards should feature Company Name and Logo.

Font styles to use
Serif

Colors

Designer to choose colors to be used in the design.

Requirements
Must have
• Strong readability of Name, phone #, mobile number and email address.
• Job title, website url, Street Address, and other details can be secondary level readability.
Nice to have
• High impact, simplistic quality design.
• Ok to utilize the 'H in the box' separate from the company name

```html
<!DOCTYPE html>
<html lang="en">
<head>
<meta charset="utf-8">
<title>Lanternfield Drinks business cards</title>
<link href="https://fonts.googleapis.com/css2?family=Tinos:wght@400;700&display=swap" rel="stylesheet">
<style>
  :root {
    --orange: #ef5a24;
    --orange-soft: #f26a3a;
    --ink: #222222;
    --ink-soft: #333333;
    --rule: #8a8a8a;
    --card: #ffffff;
    --card-shade: #ececec;
    --backdrop-dark: #000000;
    --backdrop-light: #7d7d7d;
  }
  * { margin: 0; padding: 0; box-sizing: border-box; }
  html, body { width: 1200px; height: 545px; overflow: hidden; }
  body {
    position: relative;
    background: linear-gradient(160deg, var(--backdrop-dark) 0%, #141414 45%, var(--backdrop-light) 100%);
    font-family: "Tinos", "Times New Roman", serif;
    color: var(--ink);
  }
  .card {
    position: absolute;
    top: 118px;
    width: 517px;
    height: 302px;
    border-radius: 28px;
    background: linear-gradient(200deg, var(--card) 0%, var(--card) 55%, var(--card-shade) 100%);
    box-shadow: 0 6px 14px rgba(0,0,0,0.45);
    overflow: hidden;
  }
  .card--back { left: 67px; }
  .card--front { left: 620px; height: 300px; }
  .card--front::after {
    content: "";
    position: absolute;
    left: 0; right: 0; bottom: 0;
    height: 9px;
    background: var(--orange);
  }
  .brand {
    position: absolute;
    display: flex;
    align-items: center;
    gap: 10px;
    color: var(--orange);
    font-weight: 700;
    letter-spacing: 0.5px;
    white-space: nowrap;
  }
  .brand__mark { background: var(--orange); flex: none; }
  .card--back .brand { left: 41px; top: 210px; font-size: 27px; }
  .card--back .brand__mark { width: 55px; height: 55px; }
  .card--front .brand { right: 34px; top: 98px; font-size: 24px; }
  .card--front .brand__mark { width: 40px; height: 40px; }

  .holder { position: absolute; left: 34px; top: 33px; }
  .holder__name { font-size: 19px; color: var(--ink); }
  .holder__role { font-size: 11px; color: var(--orange); margin-top: 3px; }

  .divider {
    position: absolute;
    left: 35px; right: 34px; top: 183px;
    height: 1px;
    background: var(--rule);
  }
  .contacts { position: absolute; left: 35px; top: 197px; list-style: none; }
  .contacts li {
    display: flex; align-items: center; gap: 7px;
    height: 20px; font-size: 13px; color: var(--ink-soft);
  }
  .contacts svg { width: 13px; height: 13px; flex: none; }
  .address {
    position: absolute; right: 34px; top: 198px;
    text-align: right; font-size: 12px; line-height: 18px; color: var(--ink-soft);
    font-style: normal;
  }
</style>
</head>
<body>
  <section class="card card--back" aria-label="Card back">
    <div class="brand"><span class="brand__mark"></span>LANTERNFIELD DRINKS</div>
  </section>

  <section class="card card--front" aria-label="Card front">
    <div class="holder">
      <p class="holder__name">Marcus Ellery</p>
      <p class="holder__role">Owner - Project Manager</p>
    </div>
    <div class="brand"><span class="brand__mark"></span>LANTERNFIELD DRINKS</div>
    <div class="divider"></div>
    <ul class="contacts">
      <li>
        <svg viewBox="0 0 13 13"><rect width="13" height="13" rx="2" fill="#ef5a24"/><path d="M3 4.2c0-.8.6-1.2 1.2-1.2h4.6c.6 0 1.2.4 1.2 1.2L8.6 5.4H4.4z M4.2 6.2h4.6l1 3.8H3.2z" fill="#fff"/></svg>
        402-555-0148
      </li>
      <li>
        <svg viewBox="0 0 13 13"><rect width="13" height="13" rx="2" fill="#ef5a24"/><rect x="4" y="2.5" width="5" height="8" rx="1" fill="#fff"/><rect x="4.8" y="3.4" width="3.4" height="5" fill="#ef5a24"/></svg>
        302-555-0193
      </li>
      <li>
        <svg viewBox="0 0 13 13"><rect width="13" height="13" rx="2" fill="#ef5a24"/><rect x="2.5" y="3.5" width="8" height="6" fill="#fff"/><path d="M2.5 3.5l4 3.2 4-3.2" stroke="#ef5a24" stroke-width="0.9" fill="none"/></svg>
        m.ellery@lanternfield.com
      </li>
      <li>
        <svg viewBox="0 0 13 13"><rect width="13" height="13" rx="2" fill="#ef5a24"/><circle cx="6.5" cy="6.5" r="3.8" fill="none" stroke="#fff" stroke-width="0.9"/><ellipse cx="6.5" cy="6.5" rx="1.6" ry="3.8" fill="none" stroke="#fff" stroke-width="0.8"/><path d="M2.7 6.5h7.6" stroke="#fff" stroke-width="0.8"/></svg>
        www.lanternfield.com
      </li>
    </ul>
    <address class="address">2210 Harlow Street, #118<br>Denver, CO 80205</address>
  </section>
</body>
</html>
```